Social Media Graphics - ALL TEXT KB

We are looking for a series of social media graphics for Instagram (standard size 1:1 (1080x1080px) that are ALL TEXT. We want the following quotes below on each graphic; one quote per graphic. AND, In very small letters at the bottom of each graphic, add @KBWardleOnline

The look and feel of these graphics should be complimentary to the color palette attached below; but keep them simple. But the design is up to you; at the end of this document, I provided various samples of all text graphics that I like as examples.

Target Market(s)

women looking to lose weight

Industry/Entity Type

health and wellness

Colors
E54698
E96AAD
F1A4CE
F9D9EA
FCEFF6

Requirements
Must have
• the quotes in the document
Should not have
• no stock photography

```html
<!DOCTYPE html>
<html lang="en">
<head>
<meta charset="utf-8">
<title>KB Wardle – Text Graphics Series</title>
<link href="https://fonts.googleapis.com/css2?family=League+Spartan:wght@700&family=Italiana&family=Montserrat:wght@700&display=swap" rel="stylesheet">
<style>
  :root {
    --backdrop: #f7f3f1;
    --card: #ffffff;
    --pink: #e2147f;
    --pink-soft: #f1a4ce;
    --echo: rgba(64, 200, 220, 0.75);
    --ink: #161616;
  }
  * { margin: 0; padding: 0; box-sizing: border-box; }
  html, body {
    width: 1200px; height: 1200px; overflow: hidden;
    background: var(--backdrop);
  }
  .canvas { position: relative; width: 1200px; height: 1200px; }
  .card {
    position: absolute;
    background: var(--card);
  }
  .card > * { position: absolute; }
  .headline {
    font-family: "League Spartan", "Montserrat", sans-serif;
    font-weight: 700;
    color: var(--pink);
    letter-spacing: -0.02em;
    text-shadow: -2px 2px 0 var(--echo);
    white-space: nowrap;
  }
  .statement {
    font-family: "Italiana", "Didot", serif;
    color: var(--ink);
    text-transform: uppercase;
    letter-spacing: 0.04em;
    white-space: nowrap;
  }
  .kicker {
    font-family: "League Spartan", "Montserrat", sans-serif;
    font-weight: 700;
    color: var(--pink);
    letter-spacing: -0.02em;
    white-space: nowrap;
  }
  .handle {
    font-family: "Montserrat", sans-serif;
    font-weight: 700;
    color: var(--ink);
    text-transform: uppercase;
    letter-spacing: 0.02em;
  }
  .sparkle {
    display: inline-block;
    fill: var(--pink-soft);
    vertical-align: 0.35em;
    margin-left: 2px;
  }

  /* Card: GLP-1 */
  .card--glp { left: 93px; top: 97px; width: 563px; height: 561px; }
  .card--glp .headline { left: 44px; top: 56px; font-size: 48px; line-height: 50px; }
  .card--glp .headline .lead { font-size: 38px; }
  .card--glp .statement { left: 42px; top: 215px; font-size: 84px; line-height: 78px; }
  .card--glp .kicker { left: 44px; top: 398px; font-size: 35px; line-height: 33px; }
  .card--glp .handle { left: 44px; bottom: 38px; font-size: 12px; }
  .card--glp .sparkle { width: 44px; height: 44px; }

  /* Card: bloating */
  .card--bloat { left: 709px; top: 97px; width: 414px; height: 413px; }
  .card--bloat .headline { left: 33px; top: 34px; font-size: 34px; line-height: 33px; }
  .card--bloat .statement { left: 33px; top: 110px; font-size: 48px; line-height: 46px; }
  .card--bloat .kicker { left: 33px; top: 308px; font-size: 28px; }
  .card--bloat .handle { left: 33px; top: 372px; font-size: 11px; }
  .card--bloat .sparkle { width: 32px; height: 32px; }

  /* Card: supplement */
  .card--supplement { left: 224px; top: 696px; width: 431px; height: 431px; }
  .card--supplement .headline { left: 33px; top: 48px; font-size: 46px; line-height: 42px; }
  .card--supplement .statement { left: 33px; top: 150px; font-size: 41px; line-height: 37px; }
  .card--supplement .kicker { left: 38px; top: 292px; font-size: 27px; }
  .card--supplement .handle { left: 33px; top: 388px; font-size: 11px; }
  .card--supplement .sparkle { width: 30px; height: 30px; }

  /* Card: hormones */
  .card--hormones { left: 709px; top: 553px; width: 414px; height: 414px; }
  .card--hormones .headline { left: 33px; top: 42px; font-size: 44px; line-height: 44px; }
  .card--hormones .statement { left: 33px; top: 186px; font-size: 51px; line-height: 49px; }
  .card--hormones .handle { left: 33px; top: 375px; font-size: 11px; }
  .card--hormones .sparkle { width: 30px; height: 30px; vertical-align: 0.6em; }
</style>
</head>
<body>
<main class="canvas">

  <svg width="0" height="0" aria-hidden="true" style="position:absolute">
    <defs>
      <symbol id="sparkle" viewBox="0 0 40 40">
        <path d="M20 0 L22 16 L34 6 L24 18 L40 20 L24 22 L34 34 L22 24 L20 40 L18 24 L6 34 L16 22 L0 20 L16 18 L6 6 L18 16 Z"/>
      </symbol>
    </defs>
  </svg>

  <section class="card card--glp">
    <h2 class="headline"><span class="lead">GLP-1</span><br>the magic behind the<br>weight loss drugs.</h2>
    <p class="statement">But here’s<br>the secret<svg class="sparkle" aria-hidden="true"><use href="#sparkle"/></svg></p>
    <p class="kicker">you can boost it naturally<br>without a prescription!</p>
    <p class="handle">@KBWardleOnline</p>
  </section>

  <section class="card card--bloat">
    <h2 class="headline">Struggling with<br>bloating and belly fat?</h2>
    <p class="statement">Try this<br>natural<br>solution<br>tonight<svg class="sparkle" aria-hidden="true"><use href="#sparkle"/></svg></p>
    <p class="kicker">and wake up feeling lighter!</p>
    <p class="handle">@KBWardleOnline</p>
  </section>

  <section class="card card--supplement">
    <h2 class="headline">One supplement<br>One night</h2>
    <p class="statement">Your belly bloat<br>could be gone<br>by morning.<svg class="sparkle" aria-hidden="true"><use href="#sparkle"/></svg></p>
    <p class="kicker">Here’s how it works!</p>
    <p class="handle">@KBWardleOnline</p>
  </section>

  <section class="card card--hormones">
    <h2 class="headline">Sis,<br>Your hormones are<br>out of whack</h2>
    <p class="statement">That’s why<br>the weight<br>won’t budge!<svg class="sparkle" aria-hidden="true"><use href="#sparkle"/></svg></p>
    <p class="handle">@KBWardleOnline</p>
  </section>

</main>
</body>
</html>
```